Wild Mo's Wine Label Project

We need a new entry level wine label called "Wild Mo's" for a range of wines we are developing from inland Australia. Our company is made up of three youngish guys who live hard and love taking the mickey. Wild Mo is Wild Moss - the largest and loudest of the three partners (and ideally this label will take the mickey out of him). We've grown the grapes ourselves for this first release which will be a 2012 Pinot Gris. Wine style is dry, young, fresh and contemporary and pitched at the sub AUD $10 retail price point. The package will be flint (clear) claret shape bottle with plain screwcap (colour matched to suit the winning label design).

I've attached a couple of photos of Wild Moss to give you some idea of his presence and persona.

Target Market(s)

Semi educated 25 - 40 year old wine drinkers. Skewed towards females.

Industry/Entity Type

Retail

Requirements
Should not have
• Anything traditional or old fashioned

```html
<!DOCTYPE html>
<html lang="en">
<head>
<meta charset="utf-8">
<title>Wild Mo's Pinot Gris 2012 Label</title>
<link rel="stylesheet" href="https://fonts.googleapis.com/css2?family=Philosopher:wght@400&family=Comfortaa:wght@300&family=Arimo:wght@400&display=swap">
<style>
  :root {
    --stage: #e6dcf3;
    --label-dark: #1d1d1f;
    --label-edge: #2c2c2f;
    --gold: #d6b06c;
    --ribbon-red: #8c1a20;
    --ribbon-shade: #5e1015;
    --grape-green: #7be03f;
    --grape-mid: #3f9a2a;
    --grape-deep: #1f4a17;
    --wine-red: #c8283f;
    --wine-deep: #a01e33;
    --ink-light: #f4f4f4;
  }
  html, body {
    margin: 0;
    padding: 0;
    width: 1107px;
    height: 1200px;
    overflow: hidden;
    background: var(--stage);
  }
  .canvas {
    position: relative;
    width: 1107px;
    height: 1200px;
  }
  .label {
    position: absolute;
    left: 283px;
    top: 140px;
    width: 540px;
    height: 920px;
    background: var(--label-dark);
    border: 2px solid var(--label-edge);
    border-radius: 10px;
    overflow: hidden;
  }
  .grape-cluster {
    position: absolute;
    left: 40px;
    top: 90px;
    width: 460px;
    height: 620px;
    border-radius: 46% 46% 40% 40%;
    background: radial-gradient(ellipse at 50% 48%, var(--grape-green) 0%, var(--grape-mid) 45%, var(--grape-deep) 78%, rgba(31,74,23,0) 100%);
  }
  .wine-glass {
    position: absolute;
    left: 195px;
    top: 372px;
    width: 150px;
    height: 330px;
    border-radius: 48% 48% 30% 30% / 30% 30% 12% 12%;
    background: radial-gradient(ellipse at 50% 30%, var(--wine-red) 0%, var(--wine-deep) 70%, rgba(160,30,51,0) 100%);
  }
  .brand {
    position: absolute;
    top: 150px;
    left: 0;
    width: 100%;
    margin: 0;
    text-align: center;
    font-family: "Philosopher", sans-serif;
    font-weight: 400;
    font-size: 86px;
    line-height: 1;
    color: var(--gold);
  }
  .ribbon {
    position: absolute;
    left: 10px;
    top: 258px;
    width: 520px;
    height: 110px;
  }
  .variety {
    font-family: "Comfortaa", sans-serif;
    font-weight: 300;
    fill: var(--ink-light);
  }
  .notes {
    position: absolute;
    top: 560px;
    width: 150px;
    text-align: center;
    font-family: "Arimo", sans-serif;
    color: var(--ink-light);
    line-height: 1.1;
  }
  .notes--left { left: 40px; }
  .notes--right { right: 40px; }
  .notes__main { font-size: 22px; }
  .notes__sub { font-size: 13px; }
  .details {
    position: absolute;
    top: 722px;
    left: 0;
    width: 100%;
    text-align: center;
    font-family: "Arimo", sans-serif;
    color: var(--ink-light);
    font-size: 14px;
    line-height: 1.25;
  }
  .details__closing {
    font-size: 22px;
    margin-top: 6px;
  }
</style>
</head>
<body>
<main class="canvas">
  <section class="label">
    <div class="grape-cluster" role="img" aria-label="Green grape cluster made of overlapping bubbles"></div>
    <div class="wine-glass" role="img" aria-label="Wine glass formed of red dots"></div>

    <h1 class="brand">Wild Mo's</h1>

    <svg class="ribbon" viewBox="0 0 520 110" aria-label="Pinot Gris 2012">
      <path d="M6 30 C 120 14, 260 26, 380 20 S 500 26, 514 40 L 508 98 C 420 86, 300 96, 180 92 S 40 96, 12 88 Z" fill="var(--ribbon-red)"/>
      <path d="M6 30 L 0 22 L 12 34 Z M514 40 L 520 104 L 508 98 Z" fill="var(--ribbon-shade)"/>
      <text class="variety" x="260" y="62" text-anchor="middle" font-size="46" transform="rotate(-3 260 62)">Pinot Gris</text>
      <text class="variety" x="260" y="90" text-anchor="middle" font-size="22" transform="rotate(-3 260 90)">2012</text>
    </svg>

    <div class="notes notes--left">
      <div class="notes__main">Your text</div>
      <div class="notes__sub">Your text</div>
    </div>
    <div class="notes notes--right">
      <div class="notes__main">Your text</div>
      <div class="notes__sub">Your text</div>
    </div>

    <div class="details">
      <div>Your text</div>
      <div>Your text Your text Your text</div>
      <div>Your text Your text</div>
      <div class="details__closing">Your text</div>
    </div>
  </section>
</main>
</body>
</html>
```